インターナショナル幼稚園のお誕生日カードの作成をお願い致します。

○アメリカンテイストデザインのご提案をお願い致します。
○1歳~6歳の各年齢のお誕生日にお渡しするカードです。
(1歳、2歳、3歳、4歳、5歳、6歳の6種)
テイストは同じでも構いませんが、
6種類、全て構成を別でお願い致します。(タイトル部分のフォントは同じでも可)

※添付の画像は園の先生が作成したもので、入れたい項目を記載したものです。
(参考程度に。)
初回コンペではイラストと幼稚園のロゴは低解像度のPNGデータを添付致します。
お手数ですが必要部分を切り抜いてイメージ画像の作成をお願い致します。

コンペ後、採用の方にAIデータを支給致します。(ロゴはカタカナから英語表記のものに差し替えて頂く予定です)

必須項目は
①ヌモリちゃんのイラストと園のロゴをどこかに配置。
②名前と誕生日を入れる欄は空白で作成(バースデーカード案を参照ください)
③HAPPY BIRTHDAYの文字と、年齢はそれぞれの年齢を入れて下さい。
④子どもの写真を貼るアタリはL判サイズの大きさで形は問いません。
⑤子どもの手形を押すスペースは125mm×125mm程度。手形を押すので、あまり濃い色にしないようお願いします。(形は問いません)
⑥アメリカン調で、あまり子ども子どもしていないものが好み。大人が見ても素敵だなと思う、大人よりのものがいいです。
⑦A4サイズ 4c/0c 6種類 イラストレーターCCデータ納品。
⑧最終納期は2022年4月10日。

でご提案をお待ちしております!

--
希望イメージに関して追記させていただきます。
当方の求める「アメリカンテイスト」は添付ファイルの写真のようにおしゃれなレイアウト、カラーリング、小物を希望しております。「アメコミ」のような強烈なインパクト、黒線の強すぎるものは意向と沿わない旨、ご理解願います。
こどものダミー写真サンプルを写真枠に入れていただくと、全体イメージがつかみやすく、社内会議でも好評価でした。可能な方は是非ご一考ください。
修正依頼をした為、締め切りを延長させて下さい。
たくさんのご提案ありがとうございました!
素晴らしい作品の数々に、担当者はじめ社内でも検討をするのが難しいと
うれしい悲鳴があがっております。

何名かの方々には、さらに追加修正を依頼させていただき、
お忙しい中にも手数をかけていただき、本当に感謝です。

社内検討が十分に終わりましたら、当選者を選ばせていただきますので
申し訳ありませんが、もうしばらくお待ち願います。

とてもシンプルで可愛いデザインでした。

沢山のご応募ありがとうございました。皆さんのお陰でとても良いカードができました。

```html
<!DOCTYPE html>
<html lang="ja">
<head>
<meta charset="UTF-8">
<title>Birthday Card – 1歳</title>
<link rel="stylesheet" href="https://fonts.googleapis.com/css2?family=Pacifico&family=Playfair+Display:wght@700;900&family=M+PLUS+Rounded+1c:wght@500;800&family=Quicksand:wght@600&display=swap">
<style>
  :root {
    --cream: #fbf6e8;
    --white: #ffffff;
    --mint: #86cdb0;
    --red: #d8302c;
    --navy: #2a4f86;
    --beige-text: #e3d9bd;
    --line: #e4ddc9;
    --gray: #9a9488;
    --cake: #eed3c4;
    --mascot: #e2332e;
    --gingham: #e0716a;
  }
  * { margin: 0; padding: 0; box-sizing: border-box; }
  html, body { width: 846px; height: 1200px; overflow: hidden; background: var(--cream); }
  .card {
    position: relative;
    width: 846px; height: 1200px;
    background: var(--cream);
    font-family: "M PLUS Rounded 1c", sans-serif;
    overflow: hidden;
  }
  .top-band { position: absolute; left: 0; top: 0; width: 100%; height: 40px; background: var(--mint); }
  .school-name {
    position: absolute; right: 40px; top: 74px;
    display: flex; align-items: center; gap: 10px;
    color: var(--navy); font-weight: 800; font-size: 26px;
  }
  .school-name .mark { width: 22px; height: 22px; border-radius: 50%; background: var(--navy); }
  .title-happy {
    position: absolute; left: 0; width: 660px; top: 98px; text-align: center;
    font-family: "Playfair Display", serif; font-weight: 900;
    color: var(--red); font-size: 46px; letter-spacing: 6px;
  }
  .title-birthday {
    position: absolute; left: 100px; top: 120px;
    font-family: "Pacifico", cursive; color: var(--red);
    font-size: 132px; line-height: 1.2; transform: rotate(-3deg);
  }
  .age {
    position: absolute; left: 222px; top: 288px;
    color: var(--red); font-weight: 800; font-size: 62px; line-height: 1;
  }
  .age small { font-size: 46px; }
  .cake-art {
    position: absolute; left: 335px; top: 282px; width: 148px; height: 100px;
    border-radius: 50% 50% 18px 18px / 40% 40% 18px 18px;
    background: linear-gradient(#f3e2d6, var(--cake));
  }
  .mascot-art {
    position: absolute; left: 612px; top: 160px; width: 140px; height: 165px;
    border-radius: 50% 50% 45% 45%;
    background: radial-gradient(circle at 40% 35%, #f0514a, var(--mascot));
  }
  .name-line {
    position: absolute; right: 66px; top: 400px;
    color: var(--red); font-weight: 500; font-size: 24px;
  }
  .birth-line {
    position: absolute; left: 484px; top: 468px;
    color: var(--red); font-weight: 500; font-size: 22px;
    word-spacing: 0; white-space: pre;
  }
  .handprint-box {
    position: absolute; left: 302px; top: 550px; width: 494px; height: 500px;
    background: var(--white); border-radius: 44px;
  }
  .photo-box {
    position: absolute; left: 38px; top: 425px; width: 350px; height: 292px;
    background: var(--white); border: 12px solid var(--cream); border-radius: 52px;
    display: flex; align-items: center; justify-content: center;
    font-family: "Quicksand", sans-serif; font-size: 46px; color: var(--beige-text);
    letter-spacing: 4px;
  }
  .message-label {
    position: absolute; left: 70px; top: 756px;
    font-family: "Quicksand", sans-serif; color: var(--gray); font-size: 20px; letter-spacing: 2px;
  }
  .message-label b { color: var(--red); font-size: 26px; }
  .message-lines { position: absolute; left: 70px; top: 805px; width: 186px; }
  .message-lines span { display: block; height: 49px; border-top: 2px solid var(--line); }
  .gingham-band {
    position: absolute; left: 0; bottom: 0; width: 100%; height: 128px;
    background: linear-gradient(var(--gingham), #d9605a);
  }
</style>
</head>
<body>
<main class="card">
  <div class="top-band"></div>

  <div class="school-name"><span class="mark"></span>スターリーフ</div>

  <div class="title-happy">HAPPY</div>
  <div class="title-birthday">Birthday</div>

  <div class="age">1<small>歳</small></div>
  <div class="cake-art" role="img" aria-label="いちごのケーキのイラスト"></div>
  <div class="mascot-art" role="img" aria-label="りんごのキャラクターのイラスト"></div>

  <div class="name-line">ちゃん</div>
  <div class="birth-line">令和　　年　 月　 日生まれ</div>

  <div class="handprint-box" aria-label="手形スペース"></div>
  <div class="photo-box">photo</div>

  <div class="message-label"><b>M</b>ESSAGE</div>
  <div class="message-lines"><span></span><span></span><span></span><span></span><span></span></div>

  <div class="gingham-band" role="img" aria-label="赤いギンガムチェック柄の帯"></div>
</main>
</body>
</html>
```